Brochure design for HVAC Company

A classic tri-fold brochure design for an air conditioning, refrigeration, and heating company. Would like the designs to be simple (uncluttered), professional, and pull in the logo colors. Attached is the logo and a business card designs. The company name is Bluestem Valley Air Conditioning, Refrigeration, and Heating.

Target Market(s)

Businesses normally food establishments for refrigeration and ice machines. Looking to sell them on maintenance plan: Gold, Silver, and Bronze. The material should help them to understand the services offered: Maintenance, Servicing and Troubleshooting, and Installations of ice machines, commercial refrigeration, and walk-in freezers and air conditioning (duct, ductless, and rooftop)

Industry/Entity Type

Hvac

Font styles to use
Sans Serif

Requirements
Must have
• Include standard information, such as company name, at least two types of contact information (phone, email and post office address), a logo and tagline. It should also include a headline on the front and two or three brief items outlining benefits your organization can provide.
• Tagline is approximately 14 words and 66 characters.
• Looking to inform customers of services offered: maintenance three plans gold, silver, and bronze, servicing and troubleshooting, and installation.
• Products Serviced, maintained, and installed: Commercial refrigeration, Ice Machines, Air Conditioning (both duct, ductless, and rooftop), walk in freezers.
• Call to action is $100 off on signed maintenance contract. $50 off on first service call.
• Use lorem ipsum text to complement the details of the above information. I will add it later before printing.
• Use logo color scheme and any other colors that complement it.
• Would like this to be a word template.
Nice to have
• Can you make this a Microsoft Word template? Sketch is good, or adobe cs4 format.
Should not have
• Photos should NOT be focused on the homeowner. Should BE focused on the commercial side of the business. Photos can be from any of these product areas: commercial refrigeration, ice machine, walk in freezer boxes, and light roof top ac and heating units.

```html
<!DOCTYPE html>
<html lang="en">
<head>
<meta charset="utf-8">
<title>Bluestem Valley Brochure – Outside</title>
<link rel="stylesheet" href="https://fonts.googleapis.com/css2?family=Montserrat:wght@300;400;600;700;800&display=swap">
<style>
  :root {
    --orange: #e8743b;
    --orange-deep: #e0622a;
    --blue: #2f4fa6;
    --blue-deep: #233f92;
    --white: #ffffff;
    --paper: #f1f1f1;
    --ink: #2a2f4a;
    --stage: #dfe3ea;
  }
  * { box-sizing: border-box; margin: 0; padding: 0; }
  html, body { width: 1200px; height: 900px; overflow: hidden; }
  body {
    background: var(--stage);
    font-family: "Montserrat", sans-serif;
    display: flex; align-items: center; justify-content: center;
  }
  .brochure {
    width: 1110px; height: 858px;
    display: grid; grid-template-columns: repeat(3, 1fr);
    background: var(--paper);
    box-shadow: 0 10px 30px rgba(20, 30, 60, .18);
  }
  .panel { position: relative; overflow: hidden; }

  /* Left panel: offers */
  .panel--offers svg { position: absolute; inset: 0; }
  .offers {
    position: absolute; left: 40px; bottom: 48px; color: var(--white);
  }
  .offer { margin-top: 22px; }
  .offer__amount { font-size: 34px; font-weight: 700; line-height: 1; }
  .offer__amount small { font-size: 12px; font-weight: 600; vertical-align: top; margin-left: 3px; }
  .offer__line { font-size: 19px; font-weight: 300; margin-top: 4px; }
  .offer__line b { font-weight: 700; }

  /* Middle panel: about & contact */
  .about {
    background: var(--orange); height: 46%;
    padding: 70px 38px 0 44px; color: var(--white);
  }
  .about__title { color: var(--blue); font-size: 26px; font-weight: 800; letter-spacing: .5px; margin-bottom: 16px; }
  .about__text { font-size: 12.5px; line-height: 1.65; font-weight: 400; }
  .brand-band {
    background: var(--blue); height: 14%;
    display: flex; align-items: center; padding-left: 48px;
  }
  .brand { display: flex; align-items: center; gap: 12px; color: var(--white); }
  .brand__dot { width: 30px; height: 30px; border-radius: 50%; background: var(--orange); flex: none; }
  .brand__name { font-size: 24px; font-weight: 800; line-height: 1.05; }
  .brand__sub { display: block; font-size: 7.5px; font-weight: 600; letter-spacing: .6px; margin-top: 4px; }
  .contact {
    position: relative; background: var(--white); height: 40%;
    padding: 34px 0 0 150px; color: var(--ink);
  }
  .contact__photo {
    position: absolute; left: -14px; top: -20px; width: 130px; height: 150px;
    transform: rotate(-8deg);
    background: linear-gradient(160deg, #e9eaea, #b9bcbf 60%, #8f8a80);
    border: 4px solid var(--white);
  }
  .contact__title { font-size: 18px; font-weight: 800; margin-bottom: 16px; }
  .contact__title span { color: var(--orange); font-weight: 400; }
  .contact__list { list-style: none; font-size: 12px; line-height: 1.5; }
  .contact__list li { display: flex; gap: 12px; align-items: flex-start; margin-bottom: 12px; }
  .contact__list svg { width: 16px; height: 16px; flex: none; fill: var(--blue); margin-top: 1px; }

  /* Right panel: cover */
  .cover__photo {
    height: 40%;
    background: linear-gradient(180deg, #cfc8bd 0%, #8e8a84 30%, #c7b89c 55%, #e5e2dd 100%);
  }
  .cover .brand-band { height: 12%; padding-left: 40px; }
  .cover__body { background: var(--white); height: 36%; padding: 44px 40px 0 46px; color: var(--blue); }
  .cover__headline { font-size: 25px; font-weight: 300; line-height: 1.25; }
  .cover__headline strong { display: block; color: var(--orange-deep); font-weight: 800; text-transform: uppercase; }
  .cover__foot {
    background: var(--orange-deep); height: 12%;
    display: flex; align-items: center; justify-content: flex-end; padding-right: 40px;
    color: var(--white); font-size: 22px; font-weight: 300;
  }
</style>
</head>
<body>
<main class="brochure">

  <section class="panel panel--offers">
    <svg viewBox="0 0 370 858" preserveAspectRatio="none" width="370" height="858">
      <rect width="370" height="858" fill="var(--orange-deep)"/>
      <rect width="370" height="560" fill="#b9b39d" role="img" aria-label="Photo of a commercial ice machine installed in a kitchen"/>
      <rect width="370" height="560" fill="url(#iceShade)"/>
      <polygon points="0,600 370,470 370,520 0,660" fill="var(--blue)"/>
      <polygon points="60,470 300,380 330,560 100,640" fill="var(--white)" opacity=".5"/>
      <polygon points="70,465 290,390 318,550 108,625" fill="#5b6b8e" role="img" aria-label="Photo of technicians beside rooftop solar panels"/>
      <rect x="250" y="560" width="60" height="60" fill="var(--white)" transform="rotate(-10 280 590)"/>
      <defs>
        <linearGradient id="iceShade" x1="0" y1="0" x2="1" y2="1">
          <stop offset="0" stop-color="#8d8f90" stop-opacity=".6"/>
          <stop offset=".5" stop-color="#cfcfcf" stop-opacity=".3"/>
          <stop offset="1" stop-color="#d8ccb0" stop-opacity=".4"/>
        </linearGradient>
      </defs>
    </svg>
    <div class="offers">
      <div class="offer">
        <div class="offer__amount">$100<small>OFF</small></div>
        <div class="offer__line">on signed <b>maintenance</b> contract.</div>
      </div>
      <div class="offer">
        <div class="offer__amount">$50<small>OFF</small></div>
        <div class="offer__line">on first <b>service call.</b></div>
      </div>
    </div>
  </section>

  <section class="panel panel--info">
    <div class="about">
      <h2 class="about__title">ABOUT US</h2>
      <p class="about__text">It is a long established fact that a reader will be distracted by the readable content of a page when looking at its layout. The point of using Lorem Ipsum is that it has a more-or-less normal distribution of letters, as opposed to using 'Content here, content here', making it look like readable English. Many desktop publishing packages and web page editors now use Lorem Ipsum as their default model text, and a search for 'lorem ipsum' will uncover many web sites still in their infancy. Various versions have evolved over the years, sometimes by accident, sometimes on purpose (injected humour and the like).</p>
    </div>
    <div class="brand-band">
      <div class="brand">
        <span class="brand__dot"></span>
        <div class="brand__name">Bluestem Valley<span class="brand__sub">AIR CONDITIONING • REFRIGERATION • HEATING</span></div>
      </div>
    </div>
    <div class="contact">
      <div class="contact__photo" role="img" aria-label="Photo of a stocked walk-in refrigerator interior"></div>
      <h3 class="contact__title">CONTACT <span>US</span></h3>
      <ul class="contact__list">
        <li><svg viewBox="0 0 16 16"><path d="M8 1a5 5 0 0 0-5 5c0 4 5 9 5 9s5-5 5-9a5 5 0 0 0-5-5zm0 7a2 2 0 1 1 0-4 2 2 0 0 1 0 4z"/></svg><span>PO Box 218<br>Millbrook, NY 12545</span></li>
        <li><svg viewBox="0 0 16 16"><path d="M3 1l3 3-2 2c1 2 3 4 5 5l2-2 3 3-2 3C6 15 1 10 1 4z"/></svg><span>555.014.0178</span></li>
        <li><svg viewBox="0 0 16 16"><path d="M1 3h14v10H1zm1 1v1l6 4 6-4V4z"/></svg><span>dana@bluestemhvac.com</span></li>
        <li><svg viewBox="0 0 16 16"><path d="M8 1a7 7 0 1 0 0 14A7 7 0 0 0 8 1zm0 1.5c1 1 1.6 2.6 1.8 4.5H6.2C6.4 5.1 7 3.5 8 2.5zM2.6 7h2.1c.1-1.6.5-3 1.1-4A5.5 5.5 0 0 0 2.6 7zm0 2a5.5 5.5 0 0 0 3.2 4c-.6-1-1-2.4-1.1-4zm3.6 0h3.6c-.2 1.9-.8 3.5-1.8 4.5-1-1-1.6-2.6-1.8-4.5zm5.1 0c-.1 1.6-.5 3-1.1 4a5.5 5.5 0 0 0 3.2-4zm2.1-2a5.5 5.5 0 0 0-3.2-4c.6 1 1 2.4 1.1 4z"/></svg><span>bluestemhvac.com</span></li>
      </ul>
    </div>
  </section>

  <section class="panel cover">
    <div class="cover__photo" role="img" aria-label="Photo of an open commercial refrigerated display case in a grocery store"></div>
    <div class="brand-band">
      <div class="brand">
        <span class="brand__dot"></span>
        <div class="brand__name">Bluestem Valley<span class="brand__sub">AIR CONDITIONING • REFRIGERATION • HEATING</span></div>
      </div>
    </div>
    <div class="cover__body">
      <h1 class="cover__headline">Contrary to<strong>popular belief, lorem ipsum is</strong>not simply random text</h1>
    </div>
    <div class="cover__foot">bluestemhvac.com</div>
  </section>

</main>
</body>
</html>
```